Vemb - Website Design in WordPress (2 pages)

The goal of this design work is to create two highly focused, PPC- and SEO-aware landing pages that clearly explain the experience in familiar terms and drive app installs. The design must respect the existing visual identity and support future iteration of copy and content without requiring redesign.
Required Deliverables:
Fully working WordPress site containing:
Homepage template
Location landing page template
Mobile-first, responsive
CTA behaviour exactly as designed
Required
WordPress admin access
Full site export / backup
Homepage template
Mobile-first behaviour
CTA visible above the fold on mobile
Uses my:
Visual identity
Logo
Placeholder copy
I receive:
Admin access
Full site export / backup
Not acceptable
20+ plugins
Proprietary or abandoned builders
Hardcoded layouts that can’t be reused
Separate page designs per location
Elementor is preferred if:
One builder only
Clean structure
No custom lock-in widgets
Uploaded the mobile design for inspiration only
Coding
Coded - Design and coding required
Look and feel
Each slider illustrates characteristics of the customer's brand and the style your logo design should communicate.

```html
<!DOCTYPE html>
<html lang="en">
<head>
<meta charset="utf-8">
<title>Vemb — Step Into Your Next Adventure</title>
<link href="https://fonts.googleapis.com/css2?family=Fredoka:wght@500;600;700&family=Ubuntu:wght@400;500&display=swap" rel="stylesheet">
<style>
:root{
  --teal-dark:#137f8e;
  --teal:#4cc1c9;
  --teal-pale:#d5f1f3;
  --orange:#f15a24;
  --grey:#e5e6e8;
  --ink:#333a3d;
  --white:#ffffff;
  --black:#0c0c0c;
}
*{box-sizing:border-box;margin:0;padding:0}
html,body{width:1200px;height:2938px;overflow:hidden;background:var(--white)}
body{position:relative;font-family:"Ubuntu",sans-serif;color:var(--ink)}
.abs{position:absolute}
.heading{font-family:"Fredoka",sans-serif;font-weight:600;color:var(--teal-dark)}
.brand{font-family:"Fredoka",sans-serif;font-weight:600;color:var(--teal-dark);letter-spacing:-1px}

/* store buttons */
.store{position:absolute;width:121px;height:36px;border-radius:18px;background:var(--black);color:var(--white);display:flex;align-items:center;gap:8px;padding-left:16px}
.store.light{background:var(--white);color:var(--black);box-shadow:0 2px 8px rgba(0,0,0,.08)}
.store-dot{width:14px;height:14px;border-radius:50%;background:var(--teal)}
.store.light .store-dot{background:var(--teal-dark)}
.store-text small{display:block;font-size:6px;line-height:7px;text-transform:uppercase}
.store-text b{display:block;font-size:11px;font-weight:500;line-height:12px}

/* hero */
.hero-title{left:150px;top:230px;font-size:43px;line-height:43px;width:470px}
.hero-copy{left:150px;top:367px;width:430px;font-size:12px;line-height:16px}
.drop{position:absolute}
.phone{position:absolute;background:var(--black);border-radius:34px;padding:5px}
.phone-screen{width:100%;height:100%;border-radius:29px;background:var(--teal-dark);position:relative;overflow:hidden}
.phone-notch{position:absolute;left:50%;top:9px;width:56px;height:14px;margin-left:-28px;border-radius:8px;background:var(--black)}
.splash-mark{position:absolute;left:0;right:0;top:40%;text-align:center;font-family:"Fredoka",sans-serif;font-weight:600;color:var(--white);font-size:44px}
.splash-bar{position:absolute;left:40px;right:40px;bottom:140px;height:5px;border-radius:3px;background:var(--teal)}
.splash-bar i{display:block;width:65%;height:100%;border-radius:3px;background:var(--orange)}

/* features */
.section-title{left:0;width:1200px;text-align:center;font-size:30px}
.section-sub{left:0;width:1200px;text-align:center;font-size:12px}
.photo{position:absolute}
.feature{position:absolute;left:634px;display:flex;gap:12px;align-items:center}
.feature-icon{width:55px;height:55px;border-radius:50% 50% 50% 0;background:var(--teal);display:flex;align-items:center;justify-content:center}
.feature h3{font-family:"Fredoka",sans-serif;font-weight:600;color:var(--teal-dark);font-size:15px;line-height:18px}
.feature p{font-size:12px;line-height:16px}

/* steps */
.steps-band{left:0;top:1214px;width:1200px;height:560px;border-radius:170px 170px 0 0;background:linear-gradient(180deg,var(--teal-pale) 0%,#e9f8f9 55%,var(--white) 100%)}
.step{position:absolute;top:1377px;width:200px;text-align:center}
.step-shape{width:127px;height:127px;margin:0 auto;border-radius:50% 50% 50% 0;display:flex;align-items:center;justify-content:center;position:relative}
.step-num{position:absolute;right:-16px;top:0;width:44px;height:44px;border-radius:50%;background:var(--white);font-family:"Fredoka",sans-serif;font-weight:600;font-size:18px;color:var(--teal-dark);display:flex;align-items:center;justify-content:center}
.step h3{margin-top:28px;font-family:"Fredoka",sans-serif;font-weight:600;font-size:15px;color:var(--teal-dark)}
.step p{font-size:12px;line-height:16px;margin-top:2px}

/* more */
.more-panel{left:150px;top:1698px;width:560px;height:403px;border-radius:90px 0 0 0;background:linear-gradient(90deg,var(--teal-pale) 0%,#e6f7f8 60%,rgba(255,255,255,0) 100%)}
.more-title{left:222px;top:1806px;font-size:30px;line-height:34px}
.more-copy{left:222px;top:1882px;width:340px;font-size:12px;line-height:16px}
.more-list{left:222px;top:1928px;list-style:none;font-size:12px;line-height:19px}
.more-list li::before{content:"";display:inline-block;width:5px;height:5px;border-radius:50%;background:var(--orange);margin-right:10px;vertical-align:middle}

/* trust */
.partner{position:absolute;top:2246px;width:112px;height:112px;border-radius:50%;background:var(--white);box-shadow:0 10px 24px rgba(0,0,0,.07);display:flex;align-items:center;justify-content:center}
.partner i{width:56px;height:14px;border-radius:7px;background:var(--grey)}

/* cta */
.cta-band{left:150px;top:2475px;width:899px;height:162px;border-radius:0 81px 81px 0;background:linear-gradient(90deg,#6cc6cf,var(--teal))}
.cta-title{left:222px;top:2520px;font-size:30px;line-height:35px;color:var(--white)}

/* footer */
.footer-text{left:0;width:1200px;text-align:center;top:2790px;color:var(--white);font-size:11px;line-height:14px}
.social{position:absolute;top:2835px;width:22px;height:22px;border-radius:50%;border:1px solid rgba(255,255,255,.6)}
.footer-rule{left:150px;top:2896px;width:899px;height:1px;background:rgba(255,255,255,.25)}
.copyright{left:0;width:1200px;top:2910px;text-align:center;color:var(--white);font-size:11px}
.to-top{left:1072px;top:2882px;width:30px;height:30px;border-radius:50%;background:var(--orange);display:flex;align-items:center;justify-content:center}
</style>
</head>
<body>

<!-- header -->
<div class="abs brand" style="left:150px;top:4px;font-size:50px">vemb</div>

<!-- hero -->
<h1 class="abs heading hero-title">Step Into Your Next Adventure — Anytime, Anywhere</h1>
<p class="abs hero-copy">VEMB brings real-world puzzle hunts, challenges, and adventures right to your fingertips. Play solo or with friends and explore your city like never before.</p>
<a class="store" style="left:150px;top:416px"><span class="store-dot"></span><span class="store-text"><small>Get in on</small><b>App Market</b></span></a>
<a class="store" style="left:278px;top:416px"><span class="store-dot"></span><span class="store-text"><small>Download on the</small><b>Play Hub</b></span></a>

<div class="drop" style="left:641px;top:68px;width:118px;height:120px;border-radius:59px 59px 0 0;background:var(--teal)"></div>
<div class="drop" style="left:582px;top:360px;width:125px;height:144px;border-radius:62px 62px 0 0;background:var(--orange)"></div>
<div class="drop" style="left:1049px;top:240px;width:95px;height:95px;border-radius:48px 0 48px 48px;background:var(--grey)"></div>
<div class="drop" style="left:968px;top:333px;width:142px;height:160px;border-radius:0 80px 80px 0;background:var(--teal)"></div>

<div class="phone" style="left:901px;top:160px;width:131px;height:374px">
  <div class="phone-screen" role="img" aria-label="App home screen with team progress, announcement and nearby games" style="background:linear-gradient(180deg,var(--teal-dark) 0 28%,#f3f7f8 28% 100%)"></div>
</div>
<div class="phone" style="left:699px;top:117px;width:217px;height:455px;box-shadow:0 24px 40px rgba(0,0,0,.18)">
  <div class="phone-screen">
    <div class="phone-notch"></div>
    <div class="splash-mark">vemb</div>
    <div class="splash-bar"><i></i></div>
  </div>
</div>

<!-- features -->
<h2 class="abs heading section-title" style="top:658px">Adventure, Friends &amp; Fun — All in One App</h2>
<p class="abs section-sub" style="top:702px">Join thousands of players exploring hidden stories, cracking puzzles, and connecting with friends outdoors.</p>

<div class="drop" style="left:180px;top:970px;width:185px;height:182px;border-radius:92px 0 0 0;background:var(--teal-dark)"></div>
<div class="photo" role="img" aria-label="Hands over a vintage treasure map holding a compass and a phone running the app" style="left:213px;top:749px;width:371px;height:371px;border-radius:186px 186px 186px 0;background:radial-gradient(circle at 45% 45%,#b7946b,#6b4e34);box-shadow:0 20px 40px rgba(0,0,0,.15)"></div>

<div class="feature" style="top:790px"><div class="feature-icon"><svg width="28" height="28" viewBox="0 0 24 24" fill="none" stroke="#fff" stroke-width="1.5"><circle cx="12" cy="10" r="3"/><path d="M12 21s-6-6-6-11a6 6 0 0112 0c0 5-6 11-6 11z"/></svg></div><div><h3>Explore Nearby Adventures</h3><p>Find featured games and events near you.</p></div></div>
<div class="feature" style="top:851px"><div class="feature-icon"><svg width="28" height="28" viewBox="0 0 24 24" fill="none" stroke="#fff" stroke-width="1.5"><circle cx="6" cy="9" r="2"/><circle cx="12" cy="7" r="2"/><circle cx="18" cy="9" r="2"/><path d="M3 17c0-3 6-3 6 0M9 15c0-3 6-3 6 0M15 17c0-3 6-3 6 0"/></svg></div><div><h3>Team Up or Go Solo</h3><p>Play with friends or join new players in exciting challenges.</p></div></div>
<div class="feature" style="top:910px"><div class="feature-icon"><svg width="28" height="28" viewBox="0 0 24 24" fill="none" stroke="#fff" stroke-width="1.5"><rect x="3" y="4" width="15" height="11" rx="1"/><path d="M6 12l3-3 3 2 4-4"/><circle cx="17" cy="17" r="3"/></svg></div><div><h3>Track Your Progress</h3><p>Complete missions, earn rewards, and level up.</p></div></div>
<div class="feature" style="top:971px"><div class="feature-icon"><svg width="28" height="28" viewBox="0 0 24 24" fill="none" stroke="#fff" stroke-width="1.5"><path d="M4 15c3 0 5 2 8 2s5-2 8-2M12 4v8M8 8l4 4 4-4"/></svg></div><div><h3>Flexible Fun</h3><p>Indoor and outdoor challenges for every schedule.</p></div></div>
<div class="feature" style="top:1029px"><div class="feature-icon"><svg width="28" height="28" viewBox="0 0 24 24" fill="none" stroke="#fff" stroke-width="1.5"><rect x="7" y="3" width="10" height="18" rx="2"/><path d="M11 18h2M10 9l2 2 3-3"/></svg></div><div><h3>Easy Access</h3><p>Download, join, and play in just a few taps.</p></div></div>

<!-- steps -->
<div class="abs steps-band"></div>
<h2 class="abs heading section-title" style="top:1308px">Start Your First Mission in 4 Easy Steps</h2>

<div class="step" style="left:188px">
  <div class="step-shape" style="background:var(--teal-dark)"><svg width="48" height="48" viewBox="0 0 24 24" fill="none" stroke="#fff" stroke-width="1.2"><rect x="3" y="12" width="18" height="8" rx="4"/><path d="M7 16h3M8.5 14.5v3M12 12V8a2 2 0 012-2"/><circle cx="16" cy="15" r=".6"/><circle cx="17.5" cy="17" r=".6"/></svg><span class="step-num">01</span></div>
  <h3>Browse &amp; Choose a Game</h3><p>Select from featured nearby<br>adventures.</p>
</div>
<div class="step" style="left:400px">
  <div class="step-shape" style="background:var(--orange)"><svg width="56" height="48" viewBox="0 0 28 24" fill="none" stroke="#fff" stroke-width="1.2"><circle cx="7" cy="14" r="2"/><circle cx="14" cy="14" r="2"/><circle cx="21" cy="14" r="2"/><path d="M3 21c0-4 8-4 8 0M10 21c0-4 8-4 8 0M17 21c0-4 8-4 8 0M7 10V4M5 6l2-2 2 2M14 10V3M12 5l2-2 2 2M21 10V4M19 6l2-2 2 2"/></svg><span class="step-num">02</span></div>
  <h3>Team Up</h3><p>Invite friends or join<br>existing teams.</p>
</div>
<div class="step" style="left:612px">
  <div class="step-shape" style="background:var(--teal)"><svg width="52" height="52" viewBox="0 0 24 24" fill="none" stroke="#fff" stroke-width="1.2"><circle cx="4" cy="20" r="1.5"/><circle cx="10" cy="15" r="1.5"/><circle cx="18" cy="6" r="3"/><path d="M5 19l4-3M11 15l3 1 3-6M18 9v2"/></svg><span class="step-num">03</span></div>
  <h3>Track &amp; Solve</h3><p>Follow checkpoints and solve clues<br>in real-world locations.</p>
</div>
<div class="step" style="left:825px">
  <div class="step-shape" style="background:var(--grey)"><svg width="48" height="48" viewBox="0 0 24 24" fill="none" stroke="#fff" stroke-width="1.5"><circle cx="18" cy="5" r="3"/><circle cx="6" cy="12" r="3"/><circle cx="18" cy="19" r="3"/><path d="M8.6 10.5l6.8-4M8.6 13.5l6.8 4"/></svg><span class="step-num">04</span></div>
  <h3>Complete &amp; Share</h3><p>Unlock achievements, earn rewards,<br>and share experiences.</p>
</div>

<!-- more than a game -->
<div class="abs more-panel"></div>
<h2 class="abs heading more-title">More Than Just a Game<br>It’s an Adventure</h2>
<p class="abs more-copy">VEMB blends real-world exploration, social interaction, and puzzle-solving into unforgettable experiences.</p>
<ul class="abs more-list">
  <li>Real-world location-based gameplay</li>
  <li>Social, team-oriented challenges</li>
  <li>Level progression and rewards</li>
  <li>Indoor &amp; outdoor flexibility</li>
  <li>Variety of game types: clue-hunting, puzzles, mysteries</li>
</ul>
<div class="drop" style="left:909px;top:1720px;width:102px;height:100px;border-radius:50px 0 50px 50px;background:var(--grey)"></div>
<div class="drop" style="left:659px;top:1916px;width:128px;height:137px;border-radius:64px 0 0 0;background:var(--teal)"></div>
<div class="photo" role="img" aria-label="Smiling hiker sitting on a tree in a forest holding a map and camera" style="left:721px;top:1760px;width:285px;height:282px;border-radius:142px 142px 0 142px;background:linear-gradient(160deg,#8a8f78,#4f5a3e 60%,#6b4a30)"></div>
<div class="photo" role="img" aria-label="Hands over a map with a compass and photographs" style="left:631px;top:1730px;width:188px;height:188px;border-radius:94px 94px 94px 0;background:radial-gradient(circle,#b59a74,#6d5640);border:4px solid var(--white)"></div>

<!-- trust -->
<h2 class="abs heading section-title" style="top:2193px">Trusted by Adventurers Worldwide</h2>
<div class="partner" style="left:245px" aria-label="Partner badge"><i></i></div>
<div class="partner" style="left:364px" aria-label="Partner badge"><i></i></div>
<div class="partner" style="left:484px" aria-label="Partner badge"><i></i></div>
<div class="partner" style="left:603px" aria-label="Partner badge"><i></i></div>
<div class="partner" style="left:723px" aria-label="Partner badge"><i></i></div>
<div class="partner" style="left:841px" aria-label="Partner badge"><i></i></div>

<!-- footer wave -->
<svg class="abs" style="left:0;top:2580px" width="1200" height="358" viewBox="0 0 1200 358" preserveAspectRatio="none"><path d="M0 160 C 250 60 600 60 900 20 C 1030 2 1130 -10 1200 10 L1200 358 L0 358 Z" fill="var(--teal-dark)"/></svg>

<!-- cta -->
<div class="abs cta-band"></div>
<h2 class="abs heading cta-title">Your Next Adventure<br>Is Waiting</h2>
<div class="phone" style="left:561px;top:2441px;width:144px;height:220px;border-radius:26px 26px 0 0;padding:5px 5px 0">
  <div class="phone-screen" style="border-radius:21px 21px 0 0">
    <div class="phone-notch" style="width:40px;height:10px;margin-left:-20px;top:7px"></div>
    <div class="splash-mark" style="top:92px;font-size:30px">vemb</div>
  </div>
</div>
<a class="store light" style="left:733px;top:2541px"><span class="store-dot"></span><span class="store-text"><small>Get in on</small><b>App Market</b></span></a>
<a class="store light" style="left:861px;top:2541px"><span class="store-dot"></span><span class="store-text"><small>Download on the</small><b>Play Hub</b></span></a>

<!-- footer -->
<div class="abs brand" style="left:0;width:1200px;text-align:center;top:2706px;font-size:72px;line-height:72px;color:var(--white)">vemb</div>
<p class="abs footer-text">VEMB is a location-based adventure and puzzle app that turns your city into an interactive playground. Play<br>solo or with friends and explore the world differently.</p>
<span class="social" style="left:544px" aria-label="Social link"></span>
<span class="social" style="left:574px" aria-label="Social link"></span>
<span class="social" style="left:604px" aria-label="Social link"></span>
<span class="social" style="left:634px" aria-label="Social link"></span>
<div class="abs footer-rule"></div>
<p class="abs copyright">© 2026 VEMB. All rights reserved.</p>
<a class="abs to-top" aria-label="Back to top"><svg width="10" height="10" viewBox="0 0 10 10"><path d="M2 6l3-3 3 3" fill="none" stroke="#fff" stroke-width="1.5"/></svg></a>

</body>
</html>
```